Album Artwork Design: Colorado Reggae-Funk-Hip-Hop Band

We're looking for someone to design the album artwork for our new record. The Denver, CO based reggae/rock/hip-hop/jam band is called "B-Roz and the Current". We're looking for front and back panels.

The album is called "Edge of the Lantern", talking about the seasons of life and how its all part of the ride. We were imagining two hands slightly cupped together with a light orb coming out of the palms (or one singular hand). The light has roots that go into the hands and project interesting/psychedelic objects/patterns outward. Potentially a black background.

We're open to other ideas, that was just one the band as a collective thought was cool. Would like it to be colorful and eye-catching but still clean and professional looking.

The Current depicts the band; uplifting, energetic, positive, ect.

Attached below are recordings of the songs, cool album covers we like and some rough logo ideas (please feel free to disregard if you have a better idea). Much thanks for all submissions!

Target Market(s)

Hippies, nature lovers, party people, positive people, music lovers, ect.

Industry/Entity Type

Entertainment

Logo Text

B-Roz and the Current

Requirements
Must have
• Logo for "B-Roz and the Current" - Band name
• Also on the front need "Edge of the Lantern" - Album Name
• Back side needs tracks listings and room for credits:
• 1. Toward Shores We Won't Reach
• 2. Wildflower Over Rivers
• 3. Moon Slides Down
• 4. Alleys of Tamberlin
• 5. We Could Be Free
• 6. Out In Your Glow
• 7. Raise One For Kindness
• Produced & Engineered by Dorian Pellwick & Vellbrook Audio
• © Ruben Ostrander-Hale 2017
• www.brozandthecurrent.example
Nice to have
• Elements of nature (sun, moon, trees, mountains, ect.)
• Psychedelic/visually captivating elements.
• Clean & professional color scheme/branding.
• Should be authentic and have a distinct style.
Should not have
• Anything cheesy & tacky.

```html
<!DOCTYPE html>
<html lang="en">
<head>
<meta charset="utf-8">
<title>B-Roz and the Current — Edge of the Lantern</title>
<link href="https://fonts.googleapis.com/css2?family=Montserrat:wght@500;700;800&family=Oswald:wght@400&display=swap" rel="stylesheet">
<style>
  :root {
    --stage: #808080;
    --panel-black: #050505;
    --panel-dark: #141414;
    --ink: #ffffff;
    --ink-soft: #d9d9d9;
    --glow-yellow: #e8e46a;
    --glow-green: #4f9a3a;
    --glow-deep: #1d4a2a;
    --glow-magenta: #7a2f5a;
  }
  * { box-sizing: border-box; margin: 0; padding: 0; }
  html, body {
    width: 1200px; height: 1200px; overflow: hidden;
    background: var(--stage);
  }
  .canvas {
    width: 1200px; height: 1200px;
    display: flex; align-items: center; justify-content: center; gap: 40px;
  }
  .panel {
    position: relative; width: 560px; height: 560px; overflow: hidden;
    background: var(--panel-black); color: var(--ink);
    box-shadow: 0 6px 18px rgba(0,0,0,.35);
  }

  /* Front */
  .front-art {
    position: absolute; inset: 0;
    background:
      radial-gradient(ellipse 38% 30% at 50% 52%, var(--glow-yellow) 0%, rgba(232,228,106,.55) 25%, transparent 70%),
      radial-gradient(ellipse 45% 38% at 62% 45%, var(--glow-green) 0%, rgba(79,154,58,.5) 40%, transparent 75%),
      radial-gradient(ellipse 30% 25% at 72% 60%, var(--glow-magenta) 0%, transparent 70%),
      radial-gradient(ellipse 55% 45% at 50% 50%, var(--glow-deep) 0%, transparent 80%),
      var(--panel-black);
  }
  .band-name {
    position: absolute; left: 0; right: 0; top: 205px;
    text-align: center;
    font-family: "Montserrat", sans-serif; font-weight: 800;
    font-size: 42px; line-height: 1.1; color: var(--ink);
  }
  .album-title {
    position: absolute; left: 0; right: 0; top: 462px;
    text-align: center; white-space: nowrap;
    font-family: "Oswald", sans-serif; font-weight: 400;
    font-size: 32px; line-height: 1; letter-spacing: 0.2em; color: var(--ink);
    text-transform: uppercase;
  }

  /* Back */
  .back-art {
    position: absolute; inset: 0;
    background:
      radial-gradient(ellipse 50% 60% at 75% 55%, rgba(90,90,90,.45) 0%, transparent 70%),
      radial-gradient(ellipse 40% 40% at 15% 60%, rgba(60,60,60,.35) 0%, transparent 70%),
      linear-gradient(180deg, var(--panel-dark), var(--panel-black));
  }
  .back-band-name {
    position: absolute; left: 0; right: 0; top: 40px;
    text-align: center;
    font-family: "Montserrat", sans-serif; font-weight: 800;
    font-size: 24px; line-height: 1.15; color: var(--ink);
  }
  .tracklist {
    position: absolute; left: 0; right: 0; top: 140px;
    list-style: none; text-align: center;
    font-family: "Montserrat", sans-serif; font-weight: 500;
    font-size: 21px; line-height: 1.42; text-transform: uppercase;
  }
  .credits {
    position: absolute; bottom: 36px; width: 240px;
    font-family: "Montserrat", sans-serif; font-size: 10px; line-height: 1.6;
  }
  .credits--production { left: 30px; }
  .credits--production .role { font-weight: 500; color: var(--ink-soft); font-size: 12px; }
  .credits--production .names { font-weight: 700; text-transform: uppercase; }
  .credits--rights { right: 30px; text-align: right; }
  .credits--rights .copyright { font-weight: 700; text-transform: uppercase; margin-bottom: 6px; }
  .credits--rights .site { font-weight: 500; text-transform: uppercase; }
</style>
</head>
<body>
<main class="canvas">
  <section class="panel panel--front">
    <div class="front-art" role="img" aria-label="Psychedelic glowing landscape with a tree, plants and a bright path, fading into black"></div>
    <h1 class="band-name">B-Roz<br>and the Current</h1>
    <h2 class="album-title">Edge of the Lantern</h2>
  </section>

  <section class="panel panel--back">
    <div class="back-art" role="img" aria-label="Faint grey tree silhouette texture on black"></div>
    <p class="back-band-name">B-Roz<br>and the Current</p>
    <ol class="tracklist">
      <li>1. Toward Shores We Won't Reach</li>
      <li>2. Wildflower Over Rivers</li>
      <li>3. Moon Slides Down</li>
      <li>4. Alleys of Tamberlin</li>
      <li>5. We Could Be Free</li>
      <li>6. Out In Your Glow</li>
      <li>7. Raise One For Kindness</li>
    </ol>
    <div class="credits credits--production">
      <p class="role">Produced &amp; Engineered by</p>
      <p class="names">Dorian Pellwick &amp; Vellbrook Audio</p>
    </div>
    <div class="credits credits--rights">
      <p class="copyright">© Ruben Ostrander-Hale 2017</p>
      <p class="site">www.brozandthecurrent.example</p>
    </div>
  </section>
</main>
</body>
</html>
```